CBD Boutique Business Card Needed

We are in need of a business card to reflect the direction of our latest products. We are a fully organic company in which our store and products are very heavy in wood and "natural" components. We decided to bring color into one of our brands and immediately knew this is where we needed to go.

We are NOT a cash grab CBD company. We could have done this wrong, slapped a label on a shit product and left it like that. I am passionate about sharing my experience with other veterans and opening a store and making it a comfortable place for others to come and see if they can have the same experience.

Target Market(s)

We are a dual market company. We do have a beauty line that will cover the costs of the majority of our business. But we also heavily cater to veterans and first responders. I am a veteran and this is how I found out about CBD. So the marketing needs to bring in our higher end beauty clientele but also be able to not put off our customers that readily need this.

Contact Information for Business Card

What we are looking for is a light, professional, boutique design that is is neither quite feminine or masculine. Attached is a picture of a store in Portland that we asked our store designer to get her inspiration from. But all natural wood and black outlines are what is mostly in there.

Attached are the following files:

Logo: An AI file with how we have our logo. I do not understand AI and have no idea why the letters are individual. The font is Adam. OLU is the logo and Tonics of Dawn is our tagline.

DC Portrait (front and back) cards I did originally found at a trade show that I absolutely loved...while it is mostly there and I would still be happy with them but it is me pretending to be you. I understand I am not and there is probably a lot wrong that all of you would see instantly and this is why I am here.

Dropper Bottle: This is our final product mock up

Water Color: I am semi flexible here. This water color is slightly different on every level of our brand. The color itself can change...we are not stuck on THIS particular one. If you happen to make a new one that is similar in style and we use it...then I will happily commission you to change the rest on our next product run. I am pretty sure you can use this statement as evidence later . =) .

But seriously, we heavily believe in pay it forward and will work with anyone here that may have a vision bigger than ours. The winner of this contest will get preferential consideration on our marketing materials (need letterhead etc. next, as well as a brochure, and website) so three more projects coming down the pipeline.

Information to use for your mockup is contained on the card images I have included. I would prefer CBD for wellness CBD for life to be more prominent. No where else on the card do we have CBD mentioned.

Font styles to use
Sans Serif

Colors

Designer to choose colors to be used in the design.

Requirements
Must have
• Double Sided
• Front: OLU logo on front of card will be raised embossed. Background is watercolor. One has been provided. Others are up for consideration. If the rest of your design is incredible and I don't like your watercolor I will just ask to swap it.
• Back: Standard information. Not stuck on anything here. I LOVE clean minimal designs. The bleed on the card I provided is a luxury...
• Font for title and OLU is Adam. Everything else I prefer san serif or as clean as possible.
Nice to have
• I Need to incorporate Naturally Nurturing somewhere on the card. Bold but not intrusive.

```html
<!DOCTYPE html>
<html lang="en">
<head>
<meta charset="utf-8">
<title>OLU Business Card</title>
<link rel="stylesheet" href="https://fonts.googleapis.com/css2?family=Arimo:wght@400&family=Montserrat:wght@300;400&display=swap">
<style>
  :root {
    --canvas: #ebebeb;
    --card: #ffffff;
    --ink: #1d1d1d;
    --logo-ink: #3b3d40;
    --teal: #3fb6c6;
    --teal-light: #a9dcdc;
    --sand: #f1d9a8;
    --orange: #e0913a;
    --rust: #c8702a;
  }
  * { margin: 0; padding: 0; box-sizing: border-box; }
  html, body { width: 1200px; height: 900px; overflow: hidden; }
  body {
    background: var(--canvas);
    position: relative;
    font-family: "Montserrat", sans-serif;
    color: var(--ink);
  }
  .card {
    position: absolute;
    top: 140px;
    width: 405px;
    height: 620px;
    border-radius: 16px;
    background: var(--card);
    overflow: hidden;
    box-shadow: 0 1px 3px rgba(0,0,0,0.12);
  }
  .card--back { left: 164px; }
  .card--front { left: 682px; }

  .wash { position: absolute; inset: 0; display: block; }

  .accent-bar {
    position: absolute; left: 0; top: 351px;
    width: 9px; height: 51px; background: var(--ink);
  }
  .details { position: absolute; left: 34px; top: 0; right: 20px; }
  .name {
    position: absolute; top: 350px;
    font-family: "Arimo", sans-serif; font-weight: 400;
    font-size: 26px; white-space: nowrap; letter-spacing: -0.2px;
  }
  .role { position: absolute; top: 384px; font-size: 17px; font-weight: 400; white-space: nowrap; }
  .rule { position: absolute; width: 14px; height: 2px; background: var(--ink); }
  .rule--one { top: 411px; }
  .rule--two { top: 466px; }
  .address { position: absolute; top: 420px; font-size: 15px; line-height: 18px; white-space: nowrap; }
  .contact { position: absolute; left: 0; display: flex; align-items: center; gap: 9px; font-size: 15.5px; white-space: nowrap; }
  .contact svg { width: 14px; height: 14px; flex: none; }
  .contact--phone { top: 478px; }
  .contact--mail { top: 505px; }
  .contact--web { top: 533px; }
  .slogan { position: absolute; top: 570px; font-size: 15.5px; white-space: nowrap; word-spacing: 1px; }

  .brand {
    position: absolute; left: 0; right: 0; top: 250px;
    text-align: center; color: var(--logo-ink);
    font-family: "Montserrat", sans-serif; font-weight: 300;
  }
  .brand-name { font-size: 86px; line-height: 1; letter-spacing: 4px; }
  .brand-tagline { font-size: 17px; letter-spacing: 2px; margin-top: 14px; }
</style>
</head>
<body>

  <section class="card card--back">
    <svg class="wash" viewBox="0 0 405 620" role="img" aria-label="Teal and orange watercolor wash along the top edge">
      <defs>
        <linearGradient id="wash-top" x1="0" y1="0" x2="1" y2="0.3">
          <stop offset="0" stop-color="var(--sand)"/>
          <stop offset="0.35" stop-color="var(--orange)"/>
          <stop offset="0.6" stop-color="#8fb7b0"/>
          <stop offset="0.8" stop-color="var(--teal)"/>
          <stop offset="1" stop-color="var(--teal-light)"/>
        </linearGradient>
      </defs>
      <rect width="405" height="220" fill="url(#wash-top)"/>
      <path d="M0,62 C150,62 330,100 405,196 L405,620 L0,620 Z" fill="var(--card)"/>
    </svg>

    <div class="accent-bar"></div>
    <div class="details">
      <h1 class="name">Nadia Fenwick</h1>
      <p class="role">OWNER / CEO</p>
      <span class="rule rule--one"></span>
      <p class="address">4120 N Cedar Ridge Rd Mesa,<br>AZ 85201 Suite 210</p>
      <span class="rule rule--two"></span>
      <p class="contact contact--phone">
        <svg viewBox="0 0 16 16" fill="none" stroke="currentColor" stroke-width="1.1"><path d="M3.5 1.5l2.3 2.6-1.3 1.8c.9 2 2.6 3.7 4.6 4.6l1.8-1.3 2.6 2.3-1.4 2c-5.5-.5-10-5-10.5-10.5z"/></svg>
        555.214.3080
      </p>
      <p class="contact contact--mail">
        <svg viewBox="0 0 16 16" fill="none" stroke="currentColor" stroke-width="1.1"><rect x="1" y="3.5" width="14" height="9"/><path d="M1 3.5l7 5 7-5M1 12.5l5-4.5M15 12.5l-5-4.5"/></svg>
        hello@olu.life
      </p>
      <p class="contact contact--web">
        <svg viewBox="0 0 16 16" fill="none" stroke="currentColor" stroke-width="1.1"><circle cx="8" cy="8" r="6.5"/><ellipse cx="8" cy="8" rx="3" ry="6.5"/><path d="M1.5 8h13M2.5 4.8h11M2.5 11.2h11"/></svg>
        www.olu.life
      </p>
      <p class="slogan">CBD for wellness &nbsp;CBD for life</p>
    </div>
  </section>

  <section class="card card--front">
    <svg class="wash" viewBox="0 0 405 620" role="img" aria-label="Full watercolor wash blending teal at the top right into orange at the bottom left">
      <defs>
        <linearGradient id="wash-full" x1="1" y1="0" x2="0.1" y2="1">
          <stop offset="0" stop-color="var(--teal-light)"/>
          <stop offset="0.25" stop-color="var(--teal)"/>
          <stop offset="0.5" stop-color="#d9b889"/>
          <stop offset="0.75" stop-color="var(--orange)"/>
          <stop offset="1" stop-color="var(--sand)"/>
        </linearGradient>
        <radialGradient id="wash-fade" cx="0.5" cy="0.5" r="0.6">
          <stop offset="0.75" stop-color="#fff" stop-opacity="0"/>
          <stop offset="1" stop-color="#fff" stop-opacity="0.85"/>
        </radialGradient>
      </defs>
      <rect x="0" y="0" width="405" height="620" fill="url(#wash-full)"/>
      <rect x="0" y="0" width="405" height="620" fill="url(#wash-fade)"/>
    </svg>
    <div class="brand">
      <p class="brand-name">OLU</p>
      <p class="brand-tagline">TONICS OF DAWN</p>
    </div>
  </section>

</body>
</html>
```